Project Title:
Dental Implant Overdenture Flyer (Retirement Village Target)
Objective:
Create a clean, trustworthy, and reassuring flyer aimed at older adults (60–85 years old) who struggle with loose dentures. The goal is to educate them about implant-retained “clip-on” dentures and encourage them to book a consultation.
Tone & Feel:
Warm, caring, non-intimidating
Premium but not “salesy”
Medical but easy to understand
Focus on improving quality of life (confidence, eating, comfort)
Target Audience:
Retirees / pensioners
Existing denture wearers
People frustrated with loose or uncomfortable dentures
Key Message:
“You don’t have to live with loose dentures anymore.”
Design Style:
Clean, minimal, modern
Soft colours (blues, greens, warm neutrals)
Easy-to-read large font
High contrast for older eyes
Avoid clutter
Imagery Suggestions:
Smiling older adults (natural, not stocky/overly staged)
Before/after lifestyle (eating, laughing, socialising)
Simple diagram showing denture clipping onto implants
Avoid graphic surgical images
Layout Suggestions:
A5 or DL flyer
Clear sections with headings
Icons for benefits
Strong call-to-action at bottom
HEADLINE (big and bold)
Tired of Loose Dentures?
Discover Secure “Clip-On” Teeth
🔹 PROBLEM SECTION
Do your dentures:
Slip or move when eating?
Make it hard to chew certain foods?
Feel uncomfortable or loose?
Affect your confidence when speaking or smiling?
You’re not alone — and there is a better solution.
🔹 SOLUTION SECTION
Implant-Retained “Clip-On” Dentures
We can secure your denture using just 2 dental implants, allowing your teeth to:
✔ Stay firmly in place
✔ Improve your ability to eat
✔ Feel more comfortable
✔ Boost your confidence
🔹 SIMPLE EXPLANATION (very important)
Small titanium implants are gently placed in the jaw.
Your denture then clips securely onto them, stopping movement.
🔹 PRICE SECTION (highlight this clearly)
$12,000
Includes:
2 dental implants
A brand new custom overdenture
Does not include sedation or extractions (if needed)
🔹 SEDATION
Sedation is available for comfort.
If you hold a pensioner card, you may receive a significant Vantacor rebate, often resulting in minimal out-of-pocket costs for sedation.
🔹 TRUST / REASSURANCE
Experienced implant clinician
Gentle, patient-focused care
Modern technology and techniques
🔹 CALL TO ACTION (VERY IMPORTANT)
Book a Free Consultation
📞 Call: 08 9351 4276
🌐 Visit: www.bravonclinic.com.au
📍 Located near Tallowmere shopping centre
🔹 OPTIONAL TAGLINE
Eat Better. Feel Better. Smile with Confidence Again.
Please include some photos to illustrate what a clip on denture looks like with two implants.

```html
<!DOCTYPE html>
<html lang="en">
<head>
<meta charset="utf-8">
<title>Clip-On Denture Flyers – Bravon Clinic</title>
<link href="https://fonts.googleapis.com/css2?family=Marcellus&family=Josefin+Sans:ital,wght@0,400;0,600;0,700;1,400&display=swap" rel="stylesheet">
<style>
:root{
  --page:#ece3e6;
  --paper:#f5eee3;
  --paper-warm:#efe4d3;
  --ink:#1f3640;
  --ink-soft:#2e3b40;
  --olive:#6b5a3a;
  --bronze:#8a6a40;
  --sage:#5f7f6e;
  --sage-dark:#4d6c5c;
  --navy:#27344a;
  --gold:#e9d7a6;
  --white:#ffffff;
  --card:#fbf7f0;
  --rule:#cdbfa6;
}
*{box-sizing:border-box;margin:0;padding:0}
html,body{width:1200px;height:800px;overflow:hidden;background:var(--page)}
body{position:relative;font-family:"Josefin Sans",sans-serif;color:var(--ink-soft)}
.flyer{position:absolute;top:61px;width:512px;height:644px;overflow:hidden}
.flyer--problem{left:70px;background:linear-gradient(160deg,#e6eee4 0%,#f3eee2 45%,#eef0e6 100%)}
.flyer--promise{left:620px;width:510px;background:linear-gradient(180deg,#f6efe4 0%,#f2e8d9 100%)}
.abs{position:absolute}
.serif{font-family:"Marcellus",serif}
.photo{position:absolute}
.headline{font-family:"Marcellus",serif;color:var(--ink);line-height:1.05}
.sub{font-family:"Marcellus",serif}
.checks{list-style:none}
.checks li{position:relative;padding-left:20px;white-space:nowrap}
.checks li::before{content:"";position:absolute;left:2px;top:.18em;width:5px;height:10px;border:solid currentColor;border-width:0 2px 2px 0;transform:rotate(40deg)}
.brand{font-family:"Marcellus",serif;color:var(--ink);display:flex;align-items:center;gap:8px;line-height:1.1}
.brand-dot{width:14px;height:14px;border-radius:50%;background:var(--ink);flex:none}
/* left flyer */
.problem-title{left:27px;top:22px;font-size:30px}
.problem-sub{left:29px;top:61px;font-size:19px;color:var(--olive)}
.problem-brand{left:190px;top:92px;font-size:15px}
.couple-photo{left:296px;top:41px;width:216px;height:176px;background:linear-gradient(135deg,#c8cfd0,#d9c2ab 55%,#a7b3bf);border-bottom-left-radius:60% 20%}
.problem-wave{left:0;top:96px;width:512px;height:44px}
.problem-q{left:27px;top:140px;font-size:20px;color:var(--ink)}
.problem-list{left:27px;top:168px;font-size:16px;line-height:24.5px}
.denture-illus{left:309px;top:210px;width:178px;height:112px;background:radial-gradient(ellipse at 50% 40%,#e9a9a7 0%,#e8d8c6 55%,#d9d1c4 100%);border-radius:50%}
.not-alone{left:27px;top:274px;font-size:18px;line-height:22px}
.solution-band{left:0;top:326px;width:512px;height:36px;background:linear-gradient(90deg,#e4d8bf,#efe7d6 70%,rgba(239,231,214,0));padding:8px 27px;font-family:"Marcellus",serif;font-size:20px;color:var(--ink)}
.benefits-a{left:27px;top:366px;font-size:16px;line-height:23px}
.benefits-b{left:270px;top:366px;font-size:16px;line-height:23px}
.price-card{left:25px;top:420px;width:366px;height:97px;background:var(--card);border-radius:14px;box-shadow:0 1px 4px rgba(90,70,40,.15)}
.price-amount{left:22px;top:8px;font-size:31px;color:var(--ink);font-family:"Marcellus",serif}
.price-label{left:152px;top:14px;font-size:18px;color:var(--olive);font-family:"Marcellus",serif;letter-spacing:.5px}
.price-list{left:5px;top:48px;font-size:15px;line-height:22px}
.price-note{left:262px;top:50px;font-size:9px;line-height:12px;color:#555}
.trust-tab{left:392px;top:420px;width:120px;height:97px;background:var(--sage);border-top-left-radius:16px;color:var(--white);font-size:10.5px;line-height:13px;padding:9px 6px 0 18px}
.trust-tab p+p{margin-top:4px}
.cta-bar{left:0;top:518px;width:512px;height:40px;background:var(--sage-dark);display:flex;align-items:center}
.cta-phone{display:flex;align-items:center;gap:6px;padding-left:30px;width:232px;color:var(--white);font-size:24px;font-family:"Marcellus",serif}
.cta-book{flex:1;height:30px;background:#5b7a66;border-left:3px solid var(--gold);display:flex;align-items:center;padding-left:16px;color:var(--gold);font-size:16px;font-family:"Marcellus",serif;letter-spacing:.6px}
.tagline{left:0;width:512px;text-align:center;font-style:italic;font-size:17px;color:var(--ink-soft)}
.problem-tagline{top:570px}
.problem-rule{left:20px;top:590px;width:472px;height:1px;background:var(--rule)}
.problem-foot{left:40px;top:600px;width:432px;text-align:center;font-size:11px;line-height:14px}
/* right flyer */
.promise-title{left:26px;top:29px;font-size:28px}
.woman-photo{left:240px;top:0;width:270px;height:141px;background:linear-gradient(120deg,rgba(246,239,228,0) 0%,#d9c8b3 30%,#b7a99a 70%,#c9bba6 100%)}
.promise-sub{left:26px;top:102px;font-size:18px;line-height:23px;color:var(--bronze)}
.promise-list{left:26px;top:156px;font-size:15px;line-height:22.6px}
.logo-panel{left:254px;top:141px;width:256px;height:103px;background:var(--paper-warm);padding:32px 0 0 24px}
.promise-brand{font-size:17px}
.diagram{left:22px;top:244px;width:227px;height:102px;background:linear-gradient(90deg,#e9e3d9,#e6b7b2 55%,#e2d8c9);border-radius:40% 40% 30% 30%}
.sedation-line{left:24px;top:348px;font-size:12px}
.side-price{left:279px;top:240px;width:202px;height:141px;border:1px solid var(--rule);border-top:none;border-bottom:none;text-align:center;padding-top:10px}
.side-price .amt{font-family:"Marcellus",serif;font-size:31px;color:var(--ink)}
.side-price .lbl{font-family:"Marcellus",serif;font-size:15px;color:var(--ink-soft);margin-top:2px}
.side-price .checks{display:inline-block;text-align:left;font-size:13px;line-height:20px;margin-top:10px}
.side-price .note{font-size:8px;margin-top:2px}
.includes-card{left:17px;top:372px;width:247px;height:114px;background:var(--card);border-radius:18px 0 0 0;border-left:1px solid var(--rule);border-top:1px solid var(--rule);padding:6px 0 0 20px}
.includes-card .head{display:flex;align-items:baseline;gap:8px}
.includes-card .amt{font-family:"Marcellus",serif;font-size:31px;color:var(--ink)}
.includes-card .inc{font-size:15px}
.includes-card .checks{font-size:15px;line-height:20px;margin-top:2px}
.includes-card .note{font-size:9.5px;margin-top:8px;margin-left:-14px}
.trust-card{left:260px;top:382px;width:237px;height:104px;background:var(--navy);border-radius:10px 10px 0 0;color:var(--white);padding:6px 0 0 18px}
.trust-row{display:flex;align-items:center;gap:14px;height:31px;font-size:13.5px}
.trust-row svg{flex:none}
.call-bar{left:0;top:488px;width:510px;height:76px;background:var(--navy);text-align:center;color:var(--white);padding-top:11px}
.call-bar .cta{font-family:"Marcellus",serif;font-size:22px;color:var(--gold);letter-spacing:.4px}
.call-bar .contact{display:flex;justify-content:center;align-items:center;gap:10px;font-family:"Marcellus",serif;font-size:17px;margin-top:4px}
.promise-tagline{top:577px;font-style:normal;font-size:17px}
.promise-tagline em{font-style:italic}
.promise-foot{left:40px;top:612px;width:430px;text-align:center;font-size:10px;line-height:13px}
</style>
</head>
<body>

<section class="flyer flyer--problem" aria-label="Flyer: Tired of loose dentures">
  <div class="photo couple-photo" role="img" aria-label="Photo of a smiling older couple"></div>
  <svg class="abs problem-wave" viewBox="0 0 512 44" aria-hidden="true"><path d="M0 34 C120 10 260 8 512 20" stroke="#c9bd9a" stroke-width="5" fill="none" opacity=".5"/><path d="M0 42 C140 20 280 18 512 30" stroke="#a7b8a4" stroke-width="2.5" fill="none" opacity=".45"/></svg>
  <h1 class="abs headline problem-title">Tired of Loose Dentures?</h1>
  <p class="abs sub problem-sub">Discover Secure “Clip-On” Teeth</p>
  <div class="abs brand problem-brand"><span class="brand-dot"></span><span>Bravon Clinic<br>Dental Surgery</span></div>

  <h2 class="abs serif problem-q">Do your dentures:</h2>
  <ul class="abs checks problem-list">
    <li>Slip or move when eating?</li>
    <li>Make chewing difficult?</li>
    <li>Feel loose or uncomfortable?</li>
    <li>Affect your confidence?</li>
  </ul>
  <div class="abs denture-illus" role="img" aria-label="Illustration of a denture clipping onto two implants in the jaw"></div>
  <p class="abs serif not-alone">You’re not alone — and<br>there is a better solution.</p>

  <h2 class="abs solution-band">Implant-Retained “Clip-On” Dentures</h2>
  <ul class="abs checks benefits-a"><li>Stay firmly in place</li><li>Feel more custom denture</li></ul>
  <ul class="abs checks benefits-b"><li>Eat the foods you love</li><li>Smile with confidence</li></ul>

  <div class="abs price-card">
    <span class="abs price-amount">$12,000</span>
    <span class="abs price-label">Complete Treatment</span>
    <ul class="abs checks price-list"><li>2 dental implants</li><li>Brand new custom overdenture</li></ul>
    <p class="abs price-note">◦ Sedation &amp; extractions<br>- not included.</p>
  </div>
  <div class="abs trust-tab">
    <p>Experienced implant clinician</p>
    <p>Gentle, patient focused care.</p>
    <p>Modern technology.</p>
  </div>

  <div class="abs cta-bar">
    <div class="cta-phone"><svg width="18" height="18" viewBox="0 0 24 24" aria-hidden="true"><path fill="#fff" d="M6.6 10.8a15.1 15.1 0 0 0 6.6 6.6l2.2-2.2a1 1 0 0 1 1-.25 11.4 11.4 0 0 0 3.6.57 1 1 0 0 1 1 1V20a1 1 0 0 1-1 1A17 17 0 0 1 3 4a1 1 0 0 1 1-1h3.5a1 1 0 0 1 1 1c0 1.25.2 2.450.57 3.57a1 1 0 0 1-.25 1z"/></svg>08 9351 4276</div>
    <div class="cta-book">BOOK A FREE CONSULTATION</div>
  </div>
  <p class="abs tagline problem-tagline">Eat Better. Feel Better. Smile with Confidence Again.</p>
  <div class="abs problem-rule"></div>
  <p class="abs problem-foot">If you hold a pensioner card, you may receive a significant Vantacor rebate, often resulting in minimal out-of-pocket costs for sedation.</p>
</section>

<section class="flyer flyer--promise" aria-label="Flyer: You don’t have to live with loose dentures">
  <div class="photo woman-photo" role="img" aria-label="Photo of a laughing older woman enjoying a meal"></div>
  <h1 class="abs headline promise-title">You Don’t Have to Live<br>with Loose Dentures</h1>
  <p class="abs sub promise-sub">Secure Your Smile<br>with “Clip-On” Dentures</p>
  <ul class="abs checks promise-list">
    <li>No more slipping dentures</li>
    <li>Eat comfortably again</li>
    <li>Speak with confidence</li>
    <li>Feel like yourself again</li>
  </ul>
  <div class="abs logo-panel"><div class="brand promise-brand"><span class="brand-dot"></span><span>Bravon Clinic<br>Dental Surgery</span></div></div>

  <div class="abs diagram" role="img" aria-label="Two-step diagram: implant placed, then denture clips onto two implants"></div>
  <p class="abs sedation-line">Sedation available for your comfort</p>

  <div class="abs side-price">
    <div class="amt">$12,000</div>
    <div class="lbl">Complete Treatment</div>
    <ul class="checks"><li>2 dental implants</li><li>Custom overdenture</li></ul>
    <p class="note">*Sedation &amp; extractions not included</p>
  </div>

  <div class="abs includes-card">
    <div class="head"><span class="amt">$12,000</span><span class="inc">Includes:</span></div>
    <ul class="checks"><li>2 dental implants</li><li>Custom overdenture</li></ul>
    <p class="note">*Sedation &amp; extractions not included</p>
  </div>

  <div class="abs trust-card">
    <div class="trust-row"><svg width="22" height="22" viewBox="0 0 24 24" aria-hidden="true"><circle cx="12" cy="7" r="4" fill="#e9d7a6"/><path d="M4 21c0-4.4 3.6-7 8-7s8 2.6 8 7z" fill="#e9d7a6"/></svg>Experienced clinician</div>
    <div class="trust-row"><svg width="22" height="22" viewBox="0 0 24 24" aria-hidden="true"><path d="M12 20s-7-4.3-7-9.2A3.8 3.8 0 0 1 12 8.6a3.8 3.8 0 0 1 7 2.2C19 15.7 12 20 12 20z" fill="#e9d7a6"/></svg>Gentle care approach</div>
    <div class="trust-row"><svg width="22" height="22" viewBox="0 0 24 24" aria-hidden="true"><path d="M12 2l8 3v6c0 5-3.4 9-8 11-4.6-2-8-6-8-11V5z" fill="#e9d7a6"/><path d="M8 12l3 3 5-6" stroke="#27344a" stroke-width="2" fill="none"/></svg>Trusted modern treatment</div>
  </div>

  <div class="abs call-bar">
    <div class="cta">Call Now for Your Free Consultation</div>
    <div class="contact"><svg width="16" height="16" viewBox="0 0 24 24" aria-hidden="true"><path fill="#fff" d="M6.6 10.8a15.1 15.1 0 0 0 6.6 6.6l2.2-2.2a1 1 0 0 1 1-.25 11.4 11.4 0 0 0 3.6.57 1 1 0 0 1 1 1V20a1 1 0 0 1-1 1A17 17 0 0 1 3 4a1 1 0 0 1 1-1h3.5a1 1 0 0 1 1 1c0 1.25.2 2.45.57 3.57a1 1 0 0 1-.25 1z"/></svg><span>08 9351 4276</span><span>www.bravonclinic.com.au</span></div>
  </div>
  <p class="abs tagline promise-tagline">Smile Securely Again – <em>Without Worry.</em></p>
  <p class="abs promise-foot">Sedation: with a pensioner card, you may receive a significant Vantacor rebate, often resulting in minimal sedation costs.</p>
</section>

</body>
</html>
```